political campaign lawn sign - Governor's Council in Massachuesetts

We are looking for a political lawn sign. We are running a campaign for Governor's Council in Massachusetts. This sign will be on the lawn of homes and businesses so people driving by will see it. It needs to be simple and bold. The last name is long so maybe it could say vote for Marty and then Kolbeck will be big a bold on the next line??
We need it to say:
Vote for Martin Kolbeck
Governor's Council.

Target Market(s)

local residents

Industry/Entity Type

Politcal Campaign

Font styles to use
Sans Serif
Other font styles liked:
• not sure what font but a modern looking one such as Helvetica, Arial, Sans Seri, sharp sans..

Colors
0054AA
0677BA
7BADD7
CADEEF
E8F1F8
00AB8E
00BBA5
67D7C9
C6EFE9
E9F9F6
FFF300
FFF600
FEFA6F
FFFEC7
FFFEE8

Requirements
Must have
• My name written out with a Capital D and R but lower case for every other letter so its Marty Kolbeck
Nice to have
• modern font , the Colors of the lawn sign should have Blue, Yellow and White something bold that will stand out
Should not have
• any maps of Massachusetts

```html
<!DOCTYPE html>
<html lang="en">
<head>
<meta charset="utf-8">
<title>Vote for Martin Kolbeck – Governor's Council Lawn Sign</title>
<link rel="stylesheet" href="https://fonts.googleapis.com/css2?family=Archivo+Black&family=Oswald:wght@700&display=swap">
<style>
  :root {
    --sign-yellow: #FFE000;
    --sign-navy: #09134F;
    --sign-white: #FFFFFF;
    --sign-silver: #E8E8EC;
  }
  html, body {
    margin: 0;
    padding: 0;
    width: 1200px;
    height: 900px;
    overflow: hidden;
    background: var(--sign-yellow);
  }
  .lawn-sign {
    display: block;
    width: 1200px;
    height: 900px;
  }
  .sign-border { fill: var(--sign-yellow); }
  .sign-field { fill: var(--sign-navy); }
  .sign-band-light { fill: var(--sign-white); }
  .sign-band-dark { fill: var(--sign-navy); }
  .headline, .first-name, .last-name {
    font-family: "Archivo Black", "Arial Black", sans-serif;
  }
  .headline { fill: var(--sign-white); font-size: 190px; }
  .first-name { fill: var(--sign-yellow); font-size: 298px; }
  .last-name { fill: var(--sign-silver); font-size: 128px; }
  .office {
    font-family: "Oswald", "Arial Narrow", sans-serif;
    font-weight: 700;
    font-size: 118px;
    fill: var(--sign-navy);
  }
</style>
</head>
<body>
<svg class="lawn-sign" viewBox="0 0 1200 900" xmlns="http://www.w3.org/2000/svg" role="img" aria-label="Vote for Martin Kolbeck, Governor's Council">
  <rect class="sign-border" x="0" y="0" width="1200" height="900"/>
  <rect class="sign-field" x="24" y="22" width="1155" height="624"/>
  <rect class="sign-band-light" x="24" y="646" width="1155" height="29"/>
  <rect class="sign-band-dark" x="24" y="675" width="1155" height="25"/>
  <rect class="sign-band-light" x="24" y="700" width="1155" height="178"/>

  <text class="headline" x="99" y="231" textLength="1010" lengthAdjust="spacingAndGlyphs">VOTE FOR</text>
  <text class="first-name" x="122" y="474" textLength="973" lengthAdjust="spacingAndGlyphs">MARTIN</text>
  <text class="last-name" x="114" y="600" textLength="970" lengthAdjust="spacing">KOLBECK</text>
  <text class="office" x="109" y="828" textLength="993" lengthAdjust="spacingAndGlyphs">GOVERNOR'S COUNCIL</text>
</svg>
</body>
</html>
```